Brantley Advisory Group provides support for renewable energy projects to utilities and suppliers

I need a professional looking business card that is both simple and elegant and unique. My clients are mostly large organizations not individuals. I am a consultant with my own company that is small but would like to give clients the impression I am larger. Smart grid, fiber optics, software, field hardware, distribution automation, substation automation, operations, energy storage/batteries, microgrids, customer service, strategy/roadmaps, conservation, Automated Metering Infrastruture (AMI or smart meters) are all areas of focus.

Target Market(s)

Utilities, suppliers, governmental agencies involved in energy. All types of energy especially natural gas and electrical. Especially renewable energy or green projects.

Contact Information for Business Card

Name - Mark Brantley Cell Phone - 425.318.2746 Email - mbrantley@brantleyag-example.com
Company - Brantley Advisory Group (logo) Title - Principal

Font styles to use
Serif
Sans Serif

Colors

Designer to choose colors to be used in the design.

Requirements
Must have
• Simple and professional and powerful.
• Unique/creative design.
Nice to have
• Utilize color scheme to accent logo colors. Maybe some geometric pattern on edge of card with color.
Should not have
• Busy, complicated, traditional

```html
<!DOCTYPE html>
<html lang="en">
<head>
<meta charset="UTF-8">
<title>Brantley Advisory Group — Business Card</title>
<link href="https://fonts.googleapis.com/css2?family=Open+Sans:wght@400;600&display=swap" rel="stylesheet">
<style>
  :root {
    --backdrop: #a9a9a9;
    --card: #ffffff;
    --brand-blue: #16169a;
    --brand-green: #6a8f3f;
    --ink: #222222;
  }
  * { margin: 0; padding: 0; box-sizing: border-box; }
  html, body {
    width: 1200px;
    height: 1200px;
    overflow: hidden;
    background: var(--backdrop);
    font-family: "Open Sans", Arial, sans-serif;
  }
  .canvas {
    position: relative;
    width: 1200px;
    height: 1200px;
  }
  .card {
    position: absolute;
    left: 186px;
    width: 841px;
    height: 465px;
    background: var(--card);
    border-radius: 54px;
    overflow: hidden;
  }
  .card--front { top: 115px; }
  .card--back { top: 636px; }

  .brand {
    position: absolute;
    display: flex;
    align-items: center;
    gap: 18px;
    white-space: nowrap;
  }
  .brand__mark {
    display: block;
    background: var(--brand-blue);
  }
  .brand__name {
    color: var(--brand-blue);
    font-weight: 600;
    letter-spacing: 0.2px;
  }
  .card--front .brand {
    left: 50%;
    top: 210px;
    transform: translateX(-50%);
  }
  .card--front .brand__mark { width: 36px; height: 36px; }
  .card--front .brand__name { font-size: 38px; }

  .card--back .brand {
    left: 50%;
    top: 114px;
    transform: translateX(-50%);
  }
  .card--back .brand__mark { width: 28px; height: 28px; }
  .card--back .brand__name { font-size: 30px; }

  .person {
    position: absolute;
    left: 125px;
    top: 278px;
    white-space: nowrap;
  }
  .person__name {
    color: var(--brand-blue);
    font-size: 34px;
    font-weight: 400;
    line-height: 1.1;
  }
  .person__title {
    color: var(--ink);
    font-size: 19px;
    margin-top: 6px;
    margin-left: 5px;
  }

  .divider {
    position: absolute;
    left: 405px;
    top: 240px;
    width: 2px;
    height: 142px;
    background: var(--brand-blue);
  }

  .contact {
    position: absolute;
    left: 432px;
    top: 276px;
    list-style: none;
    white-space: nowrap;
  }
  .contact__item {
    display: flex;
    align-items: center;
    gap: 12px;
    height: 26px;
    margin-bottom: 13px;
    color: var(--ink);
    font-size: 17px;
  }
  .contact__icon {
    width: 21px;
    height: 21px;
    flex: none;
  }
</style>
</head>
<body>
<main class="canvas">
  <section class="card card--front" aria-label="Card front">
    <div class="brand">
      <span class="brand__mark" aria-hidden="true"></span>
      <span class="brand__name">Brantley Advisory Group</span>
    </div>
  </section>

  <section class="card card--back" aria-label="Card back">
    <div class="brand">
      <span class="brand__mark" aria-hidden="true"></span>
      <span class="brand__name">Brantley Advisory Group</span>
    </div>

    <div class="person">
      <p class="person__name">Mark Brantley</p>
      <p class="person__title">Principal</p>
    </div>

    <div class="divider" aria-hidden="true"></div>

    <ul class="contact">
      <li class="contact__item">
        <svg class="contact__icon" viewBox="0 0 24 24" aria-hidden="true">
          <circle cx="12" cy="12" r="12" fill="var(--brand-blue)"/>
          <path d="M8.6 6.2l1.8 2.6c.3.4.2.9-.1 1.2l-.9.8c.6 1.5 1.8 2.8 3.3 3.5l.8-.9c.3-.3.8-.4 1.2-.1l2.6 1.8c.4.3.5.8.2 1.2l-.9 1.2c-.4.5-1.1.7-1.7.5-3.6-1.2-6.4-4-7.6-7.6-.2-.6 0-1.3.5-1.7l1.2-.9c.4-.3.9-.2 1.2.2z" fill="#ffffff"/>
        </svg>
        <span>425.318.2746</span>
      </li>
      <li class="contact__item">
        <svg class="contact__icon" viewBox="0 0 24 24" aria-hidden="true">
          <rect x="1" y="5" width="22" height="14" rx="1" fill="var(--brand-blue)"/>
          <path d="M2 6l10 7 10-7" fill="none" stroke="#ffffff" stroke-width="1.6"/>
        </svg>
        <span>mbrantley@brantleyag-example.com</span>
      </li>
    </ul>
  </section>
</main>
</body>
</html>
```